Amber Hollow Gathering - Promotional Poster

Amber Hollow Gathering is a party by the people, for the people. It’s where the grooviest group of creatives comes together to dream, connect, learn and inspire. This incredible forest-stomping celebration is returning in 2023 with our latest event “Velvet Jamboree”
We need your help to create consistent branding that will make the event memorable and recognisable to our attendees. To start with we need a poster announcing the festival theme and our artists for this year.
Here are the key elements we would like you to include in your design:
1. Theme: The branding should reflect the theme of "Velvet Jamboree" with vibrant colours, cosmic imagery, carnival imagery, and celestial elements. It should evoke a sense of wonder, excitement, and adventure.
2. Logo - It should include our Amber Hollow Logo. AI file attached.
3. Text - Amber Hollow (or logo) Presents Velvet Jamboree”
Must haves -
- The logo or festival name
- The Date 5-8th May 2023
- Location - Mudgee NSW
- ticket link www.amberhollowgathering.com
- artist names put in alphabetical order.
Marta Quillby
Pieter Renwold
Fig moss
Tobias Wrenfield
Murfolk
Rosie K
Nora F
Dominic Pryle
Ivo marrantes
Greta Vane
Hana P
Perdu
Vim Ostra
Otis R & Quen
4. Colour scheme: The colour scheme should be consistent with the theme of "Velvet Jamboree." We would like a range of bold and bright colours that reflect the colours of the cosmos such as purple, blue, and pink.
5. Typography: The typography should be clear and easy to read. We would like a font that reflects the Velvet Jamboree theme.
6. Graphical elements - The poster may include pictorial elements, stars, planets, moons, galaxies, carnival imagery.
7. Marketing collateral: For the winner of this project we need marketing collateral that is consistent with the branding, including artist tiles, posters, banners, social media graphics, and other promotional materials.
8. Deliverables - We need the .Ai .Id or photoshop files at the end of this project.
You can view videos & details of our past events at www.amberhollowgathering.com or on instagram.com/amber_hollow_gathering
We are excited to see your ideas and look forward to working with you

```html
<!DOCTYPE html>
<html lang="en">
<head>
<meta charset="utf-8">
<title>Amber Hollow Gathering — Velvet Jamboree 2023 Poster</title>
<link rel="stylesheet" href="https://fonts.googleapis.com/css2?family=Fraunces:opsz,wght@9..144,700;9..144,800&family=Montserrat:wght@400;500;600&display=swap">
<style>
  :root {
    --stage: #d9d9dc;
    --night-deep: #120f26;
    --night: #26204f;
    --violet: #3b2b74;
    --nebula-pink: #9c4a8c;
    --nebula-blue: #4a4fa0;
    --lilac-line: rgba(178, 160, 230, 0.55);
    --gold: #f3b55a;
    --gold-soft: #f6c47a;
    --ink-light: #f3eefa;
    --rule: rgba(243, 238, 250, 0.85);
  }
  * { margin: 0; padding: 0; box-sizing: border-box; }
  html, body { width: 1200px; height: 2303px; overflow: hidden; }
  body { background: var(--stage); position: relative; font-family: "Montserrat", sans-serif; }

  .poster {
    position: absolute; left: 60px; top: 388px;
    width: 1080px; height: 1526px; overflow: hidden;
    background: var(--night-deep);
  }
  .poster__sky {
    position: absolute; inset: 0;
    background:
      radial-gradient(circle 2px at 12% 56%, #fff, transparent),
      radial-gradient(circle 2px at 83% 49%, #fff, transparent),
      radial-gradient(circle 1.5px at 30% 14%, #fff, transparent),
      radial-gradient(circle 1.5px at 70% 12%, #fff, transparent),
      radial-gradient(circle 1.5px at 22% 44%, #fff, transparent),
      radial-gradient(circle 1.5px at 76% 68%, #fff, transparent),
      radial-gradient(ellipse 60% 30% at 35% 27%, rgba(156,74,140,0.75), transparent 70%),
      radial-gradient(ellipse 35% 25% at 88% 48%, rgba(156,74,140,0.6), transparent 70%),
      radial-gradient(ellipse 40% 30% at 70% 38%, rgba(74,79,160,0.55), transparent 70%),
      radial-gradient(circle at 50% 40%, var(--violet) 0%, var(--night) 55%, transparent 80%),
      linear-gradient(180deg, var(--night) 0%, var(--violet) 30%, var(--night) 62%, var(--night-deep) 82%);
  }
  .poster__globe { position: absolute; inset: 0; }

  .art { position: absolute; }
  .art--forest { left: 0; right: 0; top: 1150px; bottom: 0;
    background: linear-gradient(180deg, rgba(18,15,38,0) 0%, rgba(22,18,46,0.85) 22%, #110e24 60%, #0e0c1f 100%); }
  .art--dancers { left: 560px; top: 780px; width: 360px; height: 260px; border-radius: 50%;
    background: radial-gradient(ellipse at 50% 50%, rgba(120,90,170,0.28), transparent 70%); }
  .art--starburst { width: 170px; height: 170px; top: 30px; border-radius: 50%;
    background: radial-gradient(circle, rgba(200,185,245,0.35) 0%, rgba(160,140,220,0.12) 35%, transparent 70%); }
  .art--starburst-left { left: 25px; }
  .art--starburst-right { right: 25px; }
  .art--hand { width: 110px; height: 150px; top: 235px;
    background: radial-gradient(ellipse at 50% 50%, rgba(200,150,220,0.3), transparent 70%); }
  .art--hand-left { left: 5px; }
  .art--hand-right { right: 5px; }
  .art--star-column { width: 60px; top: 400px; height: 950px;
    background: repeating-linear-gradient(180deg, rgba(190,170,240,0.28) 0 14px, transparent 14px 70px);
    -webkit-mask: linear-gradient(90deg, transparent 35%, #000 35%, #000 65%, transparent 65%);
    mask: linear-gradient(90deg, transparent 35%, #000 35%, #000 65%, transparent 65%); }
  .art--star-column-left { left: 10px; }
  .art--star-column-right { right: 10px; }
  .art--moon { width: 215px; height: 260px; top: 1242px; border-radius: 50%;
    background: radial-gradient(ellipse at 50% 50%, rgba(60,50,120,0.55), rgba(40,34,90,0.2) 60%, transparent 72%); }
  .art--moon-left { left: 30px; }
  .art--moon-right { right: 30px; }
  .art--sun { left: 487px; top: 1410px; width: 100px; height: 100px; border-radius: 50%;
    background: radial-gradient(circle, rgba(120,105,190,0.45), transparent 70%); }

  .brand { position: absolute; left: 0; right: 0; top: 108px; text-align: center; color: var(--gold); }
  .brand__name { font-size: 27px; font-weight: 400; letter-spacing: 0.42em; padding-left: 0.42em; }
  .brand__sub { margin-top: 6px; font-size: 13px; font-weight: 400; letter-spacing: 0.9em; padding-left: 0.9em; }

  .presents {
    position: absolute; left: 0; right: 0; top: 258px;
    display: flex; justify-content: center; align-items: center; gap: 22px;
    color: var(--ink-light); font-size: 36px; font-weight: 400; letter-spacing: 0.08em;
  }
  .presents::before, .presents::after { content: ""; width: 78px; height: 2px; background: var(--rule); }

  .title { position: absolute; left: 0; right: 0; top: 304px; text-align: center; color: var(--gold);
    font-family: "Fraunces", serif; font-weight: 800; line-height: 1;
    font-variation-settings: "opsz" 36; }
  .title__name { font-size: 96px; }
  .title__year { font-size: 130px; margin-top: 0; }

  .facts { position: absolute; left: 180px; width: 720px; top: 560px; height: 88px;
    border-bottom: 2px solid var(--rule); display: flex; }
  .facts__item { flex: 1; text-align: center; }
  .facts__item + .facts__item { border-left: 2px solid var(--rule); }
  .facts__label { color: var(--ink-light); font-size: 25px; letter-spacing: 0.08em; line-height: 1; margin-top: 4px; }
  .facts__value { color: var(--gold); font-family: "Fraunces", serif; font-weight: 700; font-size: 42px; line-height: 1.15;
    font-variation-settings: "opsz" 36; }

  .ticket { position: absolute; left: 180px; top: 668px; width: 720px; height: 52px;
    border: 2px solid var(--gold); border-radius: 26px; display: flex; align-items: center; overflow: hidden; }
  .ticket__label { width: 210px; text-align: center; color: var(--ink-light); font-size: 23px; letter-spacing: 0.04em; }
  .ticket__url { flex: 1; height: 100%; background: var(--gold); border-radius: 26px;
    display: flex; align-items: center; justify-content: center;
    color: var(--night); font-size: 21px; letter-spacing: 0.06em; font-weight: 500; }
  .ticket__url b { font-weight: 600; }

  .mask-art { position: absolute; left: 437px; top: 756px; width: 206px; height: 112px;
    border-radius: 50% 50% 45% 45%;
    background: radial-gradient(ellipse at 50% 45%, var(--gold-soft), #e07a3a 60%, var(--nebula-pink) 100%); }

  .artists { position: absolute; left: 290px; width: 500px; top: 876px; }
  .artists__heading { text-align: center; color: var(--ink-light); font-size: 32px; font-weight: 400; letter-spacing: 0.1em;
    padding-bottom: 6px; border-bottom: 2px solid var(--rule); }
  .artists__columns { display: flex; position: relative; padding-top: 12px; }
  .artists__columns::after { content: ""; position: absolute; left: 249px; top: 0; width: 2px; height: 326px; background: var(--rule); }
  .artists__list { flex: 1; list-style: none; text-align: center; color: var(--gold);
    font-family: "Fraunces", serif; font-weight: 700; font-size: 29px; line-height: 43.5px;
    font-variation-settings: "opsz" 24; }
  .artists__list:first-child { margin-left: -70px; }
  .artists__list:last-child { margin-right: -70px; }
</style>
</head>
<body>
  <main class="poster">
    <div class="poster__sky" role="img" aria-label="Cosmic nebula sky in purple, pink and blue with scattered stars"></div>
    <svg class="poster__globe" width="1080" height="1526" viewBox="0 0 1080 1526" aria-hidden="true">
      <circle cx="540" cy="600" r="560" fill="rgba(90,70,160,0.10)" stroke="var(--lilac-line)" stroke-opacity="0.35" stroke-width="2"/>
    </svg>
    <div class="art art--dancers" role="img" aria-label="Faint silhouettes of dancing festival-goers"></div>
    <div class="art art--forest" role="img" aria-label="Pine forest and mountain silhouette"></div>
    <div class="art art--starburst art--starburst-left" role="img" aria-label="Line-drawn starburst with small stars"></div>
    <div class="art art--starburst art--starburst-right" role="img" aria-label="Line-drawn starburst with small stars"></div>
    <div class="art art--hand art--hand-left" role="img" aria-label="Line-drawn reaching hand"></div>
    <div class="art art--hand art--hand-right" role="img" aria-label="Line-drawn reaching hand"></div>
    <div class="art art--star-column art--star-column-left" role="img" aria-label="Column of line-drawn stars"></div>
    <div class="art art--star-column art--star-column-right" role="img" aria-label="Column of line-drawn stars"></div>
    <div class="art art--moon art--moon-left" role="img" aria-label="Line-drawn crescent moon"></div>
    <div class="art art--moon art--moon-right" role="img" aria-label="Line-drawn crescent moon"></div>
    <div class="art art--sun" role="img" aria-label="Line-drawn sun"></div>

    <header class="brand">
      <div class="brand__name">AMBER HOLLOW</div>
      <div class="brand__sub">GATHERING</div>
    </header>

    <p class="presents">PRESENTS</p>

    <h1 class="title">
      <div class="title__name">Velvet Jamboree</div>
      <div class="title__year">2023</div>
    </h1>

    <section class="facts">
      <div class="facts__item">
        <p class="facts__label">DATE</p>
        <p class="facts__value">5th-8th May</p>
      </div>
      <div class="facts__item">
        <p class="facts__label">LOCATION</p>
        <p class="facts__value">Mudgee NSW</p>
      </div>
    </section>

    <div class="ticket">
      <span class="ticket__label">TICKET LINK</span>
      <span class="ticket__url">WWW.<b>AMBERHOLLOWGATHERING</b>.COM</span>
    </div>

    <div class="mask-art" role="img" aria-label="Ornate golden carnival masquerade mask illustration"></div>

    <section class="artists">
      <h2 class="artists__heading">ARTISTS</h2>
      <div class="artists__columns">
        <ul class="artists__list">
          <li>Dominic Pryle</li>
          <li>Fig moss</li>
          <li>Greta Vane</li>
          <li>Hana P</li>
          <li>Ivo marrantes</li>
          <li>Marta Quillby</li>
          <li>Murfolk</li>
        </ul>
        <ul class="artists__list">
          <li>Nora F</li>
          <li>Otis R &amp; Quen</li>
          <li>Perdu</li>
          <li>Pieter Renwold</li>
          <li>Rosie K</li>
          <li>Tobias Wrenfield</li>
          <li>Vim Ostra</li>
        </ul>
      </div>
    </section>
  </main>
</body>
</html>
```